High end cable company busines card and letterhead

Dear designers,
We assemble high end audio cables that cost a couple of hundred dollars per piece and we are improving the looks of the product.
When people buy a cable they get a leather pouch with the invoice (letterhead) , a business card of the maker and also a quality control card  / warranty card.
The quality control card  is the same size as a business card and the back of the quality control card is the same back as the business card. So we need 4 things:
-1 back of a business card
-1 front of a business card (a file where we can change the name and details of the worker)
-1 quality control front (I will add a photo of an example)
-1 letterhead
We want to make letterpress business cards and use shiny foil for the logo’s. We like the colors black and copper or black and gold for the back. The front of the business card can also be black, copper and white but it does not have to be those colors. We want people to have the feeling that they bought something expensive and high quality.
The front of the quality control card has to be white so we can check things off with a sharpie / pen.
What has to be on the cards:
Business card:
- Our Logo
-Text: Meet the maker (people get the business card of the one who made the cable)
-Name
-Address
-Website (www.tarvelinkaudio.com)
-Email address
-Text: For any advise or questions about your cable feel free to contact me.
What has to be on the quality control card:
-Our logo
-Text: quality controll and warranty card (small at the bottom)
-text:
Assembled by:________________
Date: ______-______-____________
QC by:_________________________

Assembly QC [   ]
Measurement QC [   ]
Aesthetics [   ]
(The box [    ] is for the initials of the person that does the QC, it can also be a line or something else)
The letterhead can be your own idea as long as it looks luxurious.
You can download our logo. We have a black one and gold / black but you can change the Color to Match your design. (For instance copper or something) There is also a white one that can be used with the icon on the left.
Some links of stuff we like:
-https://vidlumo.example/k3RzQ81wXyT (The looks of this card maybe a bit less busy looking)
-https://b.shopvarna.com/_qTrwBxe
-https://b.shopvarna.com/_qHp4Lud
-https://b.shopvarna.com/_qZeyi71

```html
<!DOCTYPE html>
<html lang="en">
<head>
<meta charset="utf-8">
<title>Tarvelink Business Card</title>
<link rel="stylesheet" href="https://fonts.googleapis.com/css2?family=Poppins:wght@400;500&family=Josefin+Sans:wght@400;600&family=Dancing+Script:wght@500&display=swap">
<style>
  :root {
    --backdrop: #e3e3e6;
    --card: #f4f4f4;
    --ink: #1c1c1c;
    --band: #1e1e1e;
    --emboss: #cfcfd1;
    --paper-text: #ffffff;
    --rule: #2a2a2a;
  }
  * { margin: 0; padding: 0; box-sizing: border-box; }
  html, body { width: 1200px; height: 862px; overflow: hidden; }
  body {
    background: var(--backdrop);
    font-family: "Poppins", sans-serif;
    color: var(--ink);
    position: relative;
  }
  .sheet-title {
    position: absolute; left: 48px; top: 28px;
    font-size: 28px; font-weight: 400; letter-spacing: 0.3px;
  }
  .card {
    position: absolute; top: 290px;
    width: 520px; height: 297px;
    background: var(--card);
    box-shadow: 0 10px 26px rgba(0,0,0,0.12);
    overflow: hidden;
  }
  .card--front { left: 50px; }
  .card--back { left: 630px; }

  .brand-name {
    font-family: "Josefin Sans", sans-serif;
    font-weight: 400;
    color: var(--emboss);
    letter-spacing: 10px;
    text-transform: uppercase;
  }
  .card--front .brand-name {
    position: absolute; left: 0; right: 0; top: 92px;
    text-align: center; font-size: 44px;
  }
  .tagline {
    position: absolute; left: 0; right: 0; top: 172px;
    text-align: center;
    font-family: "Dancing Script", cursive;
    font-size: 34px; font-weight: 500;
  }

  .card--back .brand-name {
    position: absolute; left: 30px; top: 62px;
    font-size: 26px; letter-spacing: 7px;
  }
  .maker-name {
    position: absolute; right: 30px; top: 30px;
    font-family: "Josefin Sans", sans-serif;
    font-weight: 600; font-size: 24px; letter-spacing: 1px;
  }
  .maker-rule {
    position: absolute; right: 24px; top: 66px;
    width: 220px; height: 1.5px; background: var(--rule);
  }
  .contact-list {
    position: absolute; left: 270px; top: 80px;
    list-style: none; font-size: 11px; line-height: 1.35;
  }
  .contact-list li {
    display: flex; align-items: flex-start; gap: 8px; margin-bottom: 6px;
  }
  .contact-list svg { flex: none; width: 16px; height: 16px; }
  .contact-list .gap { margin-top: 6px; }
  .note-band {
    position: absolute; left: 0; right: 0; bottom: 0; height: 74px;
    background: var(--band);
    display: flex; align-items: center; justify-content: center;
    padding: 0 24px;
  }
  .note-band p {
    font-family: "Dancing Script", cursive;
    color: var(--paper-text); font-size: 19px; font-weight: 500;
  }
</style>
</head>
<body>
  <h1 class="sheet-title">Business Card Mockup 1</h1>

  <section class="card card--front" aria-label="Business card front">
    <div class="brand-name">Tarvelink</div>
    <p class="tagline">Meet The Maker</p>
  </section>

  <section class="card card--back" aria-label="Business card back">
    <div class="brand-name">Tarvelink</div>
    <h2 class="maker-name">OWEN HARTLEY</h2>
    <div class="maker-rule"></div>
    <ul class="contact-list">
      <li>
        <svg viewBox="0 0 16 16" aria-hidden="true"><circle cx="8" cy="8" r="7.2" fill="none" stroke="#1c1c1c" stroke-width="1"/><path d="M5.6 4.4l1.3 1.6-.8 1a5 5 0 0 0 2.9 2.9l1-.8 1.6 1.3-.8 1.2c-3 .2-6.2-3-6-6z" fill="#1c1c1c"/></svg>
        <span>(555) 014-2286</span>
      </li>
      <li>
        <svg viewBox="0 0 16 16" aria-hidden="true"><circle cx="8" cy="8" r="7.2" fill="none" stroke="#1c1c1c" stroke-width="1"/><rect x="4.3" y="5.3" width="7.4" height="5.4" fill="#1c1c1c"/><path d="M4.3 5.5L8 8.3l3.7-2.8" fill="none" stroke="#f4f4f4" stroke-width="0.8"/></svg>
        <span>info@tarvelinkaudio.com</span>
      </li>
      <li>
        <svg viewBox="0 0 16 16" aria-hidden="true"><circle cx="8" cy="8" r="7.2" fill="none" stroke="#1c1c1c" stroke-width="1"/><circle cx="8" cy="8" r="3.8" fill="none" stroke="#1c1c1c" stroke-width="0.9"/><ellipse cx="8" cy="8" rx="1.6" ry="3.8" fill="none" stroke="#1c1c1c" stroke-width="0.8"/><path d="M4.2 8h7.6" stroke="#1c1c1c" stroke-width="0.8"/></svg>
        <span>www.tarvelinkaudio.com</span>
      </li>
      <li class="gap">
        <svg viewBox="0 0 16 16" aria-hidden="true"><circle cx="8" cy="8" r="7.2" fill="none" stroke="#1c1c1c" stroke-width="1"/><path d="M8 12.2s-3-3.2-3-5.2a3 3 0 0 1 6 0c0 2-3 5.2-3 5.2z" fill="#1c1c1c"/><circle cx="8" cy="7" r="1" fill="#f4f4f4"/></svg>
        <span>1742 Alder Brook Rd, Fenwick Valley<br>Oregon 97990</span>
      </li>
    </ul>
    <div class="note-band">
      <p>for any advise or questions about your cable feel free to contact me</p>
    </div>
  </section>
</body>
</html>
```